Need a redesign for our Wordpress Credit report website

Hi, We need someone to redesign our Wordpress credit report website, brightledgerview.co.za. The designer will be responsible for the following pages:
- home page
- blog page
- single post
- dashboard
- credit report page

About BrightLedgerView.co.za
Bright Ledger View is a consumer focussed credit report platform where South African citizens can get an easy to understand credit report that shows them where to improve their credit scores.

```html
<!DOCTYPE html>
<html lang="en">
<head>
<meta charset="utf-8">
<title>Bright Ledger View – Check your credit score</title>
<link href="https://fonts.googleapis.com/css2?family=Fira+Sans:wght@400;500;600;700&display=swap" rel="stylesheet">
<style>
:root{
  --blue:#1a73c8;
  --blue-dark:#0f5bb0;
  --green:#9acd32;
  --green-soft:#e6f2cf;
  --navy:#06142b;
  --ink:#111111;
  --grey:#555;
  --white:#fff;
}
*{margin:0;padding:0;box-sizing:border-box}
html,body{width:1200px;height:3606px;overflow:hidden}
body{position:relative;font-family:"Fira Sans",Arial,sans-serif;color:var(--ink);background:var(--green-soft)}
.abs{position:absolute}
a{color:inherit;text-decoration:none}

/* top bar */
.topbar{left:0;top:0;width:1200px;height:38px;background:var(--blue);color:var(--white);font-size:13px;font-weight:500}
.topbar .promo{left:112px;top:11px}
.topbar .call{right:113px;top:11px;display:flex;align-items:center;gap:10px}
.topbar .call i{width:20px;height:20px;border-radius:50%;background:var(--green);display:inline-block}

/* hero */
.hero{left:0;top:38px;width:1200px;height:816px;background:linear-gradient(100deg,#f4f4f4 0%,#e9e9ea 40%,#d8d6d3 70%,#c9c2ba 100%)}
.header{left:0;top:38px;width:1200px;height:130px}
.logo{left:112px;top:108px;display:flex;align-items:center;gap:10px;font-size:26px;font-weight:500;color:var(--blue)}
.logo i{width:36px;height:36px;border-radius:50%;background:var(--green);display:inline-block}
.nav{top:106px;left:534px;display:flex;gap:36px;font-size:13px;font-weight:500;color:#333;letter-spacing:.3px}
.btn-login{left:892px;top:97px;width:89px;height:32px;border:2px solid var(--blue);border-radius:16px;color:var(--blue);font-size:14px;font-weight:700;text-align:center;line-height:28px}
.btn-signup{left:997px;top:97px;width:90px;height:32px;border-radius:16px;background:linear-gradient(90deg,var(--blue),var(--green));color:var(--white);font-size:14px;font-weight:700;text-align:center;line-height:32px}

/* score form */
.score-card{left:112px;top:757px;width:975px;height:362px;background:var(--white);box-shadow:0 4px 14px rgba(0,0,0,.06)}
.score-card h1{position:absolute;left:0;top:47px;width:100%;text-align:center;font-size:34px;font-weight:700}
.accent{color:var(--blue)}
.field{position:absolute;top:135px;width:195px}
.field label{display:block;font-size:13px;color:#333;margin-bottom:12px}
.field .input{height:52px;border:1.5px solid #bbb;font-size:13px;color:#444;padding:16px 0 0 20px}
.agree{position:absolute;left:76px;top:237px;font-size:11.5px;color:#333;display:flex;align-items:center;gap:10px}
.agree i{width:13px;height:13px;border:1px solid #999;display:inline-block}
.disclaimer{position:absolute;left:76px;top:272px;width:560px;font-size:11.5px;line-height:18px;color:#444}
.btn-score{position:absolute;left:735px;top:272px;width:164px;height:37px;border-radius:19px;background:linear-gradient(90deg,var(--blue),var(--green));color:var(--white);font-size:14px;font-weight:700;text-align:center;line-height:37px}

/* about */
.about-photo{left:112px;top:1222px;width:487px;height:486px;background:linear-gradient(135deg,#f1f1ee 0%,#bcd9c9 45%,#16b394 70%,#7d8c95 100%);outline:14px solid #eef6dd}
.about-panel{left:477px;top:1317px;width:610px;height:521px;background:var(--green);color:var(--white)}
.about-panel h2{position:absolute;left:181px;top:74px;font-size:34px;font-weight:700}
.about-panel h2 span{color:var(--blue)}
.about-panel p{position:absolute;left:181px;width:380px;font-size:12.5px;line-height:22px}
.about-list{position:absolute;left:181px;top:318px;list-style:none;font-size:12.5px}
.about-list li{display:flex;align-items:center;gap:14px;height:35px}
.about-list svg{flex:none}

/* why choose */
.why{left:0;top:1954px;width:1200px;height:672px;background:linear-gradient(120deg,#1c68c6 0%,#2a83dd 45%,#1560bd 100%);color:var(--white)}
.why h2{position:absolute;left:0;top:98px;width:100%;text-align:center;font-size:34px;font-weight:700}
.feature{position:absolute;font-size:13px;line-height:21px}
.feature.right-al{text-align:right}
.device{left:437px;top:2351px;width:330px;height:275px;background:linear-gradient(180deg,#2c2f36 0%,#e4e6ea 60%,#c3c6cc 100%);border-radius:8px 8px 0 0}

/* why us */
.why-us h2{position:absolute;left:0;top:2730px;width:1200px;text-align:center;font-size:34px;font-weight:700}
.step{position:absolute;left:221px;width:50px;height:50px;border-radius:50%;border:3px solid var(--green);background:#dbeec0;color:var(--blue);font-size:16px;font-weight:700;text-align:center;line-height:44px}
.step-title{position:absolute;left:290px;font-size:15px;font-weight:700}
.step-body{position:absolute;left:290px;top:2868px;width:690px;font-size:12.5px;line-height:22px;color:#444}
.timeline{left:245px;top:2867px;width:2px;height:190px;background:var(--blue)}
.step-arrow{left:235px;top:2908px;width:22px;height:22px;border-radius:50%;background:var(--ink)}

/* footer */
.footer{left:0;top:3210px;width:1200px;height:396px;background:var(--navy);color:var(--white)}
.footer-about{left:112px;top:3312px;width:310px;font-size:14px;line-height:27px}
.socials{left:112px;top:3433px;display:flex;gap:15px}
.socials i{width:28px;height:28px;border-radius:50%;background:var(--white);display:block}
.links{top:3312px;list-style:none;font-size:14px;font-weight:500;line-height:27px}
.contact-icon{width:50px;height:50px;border-radius:50%;border:2px solid var(--white)}
.contact-label{font-size:20px;font-weight:700}
.contact-value{font-size:13px}
.copyright{left:0;top:3538px;width:1200px;text-align:center;font-size:13px}
.btn-demo{left:974px;top:3504px;width:195px;height:45px;border-radius:23px;background:var(--green);color:var(--navy);font-size:13px;font-weight:700;display:flex;align-items:center;justify-content:center;gap:14px}
</style>
</head>
<body>

<div class="abs topbar">
  <span class="abs promo">CHECK YOUR CREDIT SCORE WITHIN SECONDS</span>
  <span class="abs call"><i></i>Call Us Now : 876 555-0142</span>
</div>

<div class="abs hero" role="img" aria-label="Photo of a man typing on a laptop showing a sample credit report with a score gauge"></div>

<div class="abs logo"><i></i>Bright Ledger View</div>
<nav class="abs nav"><a>HOME</a><a>ARTICLES</a><a>ABOUT US</a><a>CONTACT US</a></nav>
<a class="abs btn-login">LOGIN</a>
<a class="abs btn-signup">SIGN UP</a>

<section class="abs score-card">
  <h1>CHECK YOUR CREDIT SCORE <span class="accent">WITHIN SECONDS</span></h1>
  <div class="field" style="left:76px"><label>ID Number</label><div class="input">000 000-0000</div></div>
  <div class="field" style="left:286px"><label>Full Name</label><div class="input">Sam Peters</div></div>
  <div class="field" style="left:496px"><label>Primary Email</label><div class="input">sam@mailbox.com</div></div>
  <div class="field" style="left:706px"><label>Mobile Number</label><div class="input">000 000-0000</div></div>
  <div class="agree"><i></i>I agree with the terms and conditions</div>
  <p class="disclaimer">By signing up and agreeing with the terms you authorise BrightLedgerView.co.za to request your credit report from the bureaus and display it within the site.</p>
  <a class="btn-score">SHOW MY SCORE</a>
</section>

<section>
  <div class="abs about-panel">
    <h2>ABOUT <span>US</span></h2>
    <p style="top:141px">brightledgerview.co.za (BLV) is a web based platform that enables credit active consumers to get direct access to their credit scores and profiles in an easy to understand and interactive online report.</p>
    <p style="top:228px">BLV launched in November 2013 and has since helped thousands of South Africans get access to their credit reports, many people becoming regular users on our platform</p>
    <ul class="about-list">
      <li><svg width="20" height="20" viewBox="0 0 20 20"><circle cx="10" cy="10" r="10" fill="#fff"/><path d="M5 10h9M10 6l4 4-4 4" stroke="#9acd32" stroke-width="2" fill="none"/></svg>See your most recent credit score.</li>
      <li><svg width="20" height="20" viewBox="0 0 20 20"><circle cx="10" cy="10" r="10" fill="#fff"/><path d="M5 10h9M10 6l4 4-4 4" stroke="#9acd32" stroke-width="2" fill="none"/></svg>Get access to your full credit profile.</li>
      <li><svg width="20" height="20" viewBox="0 0 20 20"><circle cx="10" cy="10" r="10" fill="#fff"/><path d="M5 10h9M10 6l4 4-4 4" stroke="#9acd32" stroke-width="2" fill="none"/></svg>See who has been looking at your profile.</li>
      <li><svg width="20" height="20" viewBox="0 0 20 20"><circle cx="10" cy="10" r="10" fill="#fff"/><path d="M5 10h9M10 6l4 4-4 4" stroke="#9acd32" stroke-width="2" fill="none"/></svg>See if you have any adverse or Blacklistings.</li>
    </ul>
  </div>
  <div class="abs about-photo" role="img" aria-label="Hands typing on a laptop whose screen shows a credit score gauge from poor to good, with a pencil cup behind"></div>
</section>

<section class="abs why">
  <h2>WHY CHOOSE US</h2>
  <svg class="abs" style="left:0;top:0" width="1200" height="672" viewBox="0 1954 1200 672">
    <circle cx="596" cy="2495" r="268" fill="none" stroke="rgba(255,255,255,.35)" stroke-width="1.5"/>
    <g fill="#fff" stroke="#9acd32" stroke-width="4">
      <circle cx="592" cy="2227" r="25"/><circle cx="442" cy="2271" r="25"/><circle cx="745" cy="2271" r="25"/>
      <circle cx="340" cy="2401" r="25"/><circle cx="846" cy="2401" r="25"/><circle cx="335" cy="2558" r="25"/><circle cx="857" cy="2558" r="25"/>
    </g>
    <g fill="none" stroke="#222" stroke-width="1.6">
      <rect x="582" y="2218" width="20" height="18"/><path d="M586 2224h12M586 2230h12"/>
      <path d="M430 2276a12 12 0 0 1 24 0M442 2276l5-6"/>
      <rect x="733" y="2262" width="24" height="16"/><path d="M740 2283h10"/>
      <rect x="331" y="2391" width="18" height="20"/><path d="M335 2397h10M335 2403h10"/>
      <rect x="834" y="2390" width="24" height="16"/><path d="M840 2412h12"/>
      <circle cx="335" cy="2558" r="8"/><circle cx="335" cy="2558" r="3"/>
      <circle cx="857" cy="2558" r="12"/>
    </g>
    <text x="857" y="2562" font-family="Fira Sans,sans-serif" font-size="9" font-weight="700" text-anchor="middle" fill="#222">24/7</text>
  </svg>
  <div class="feature" style="left:492px;top:189px;width:200px;text-align:center">Personal Budgeting<br>Spreadsheet</div>
  <div class="feature right-al" style="left:199px;top:296px;width:200px">Improve your credit score<br>eBook</div>
  <div class="feature" style="left:794px;top:307px">Perfect score video course</div>
  <div class="feature right-al" style="left:98px;top:425px;width:200px">Budget tool - easily create<br>a budget</div>
  <div class="feature" style="left:895px;top:425px">Personal Finance Video<br>Tutorials</div>
  <div class="feature right-al" style="left:94px;top:583px;width:200px">Dispute generator - Easily<br>manage disputes</div>
  <div class="feature" style="left:904px;top:594px">Dedicated 24/7 Support</div>
</section>
<div class="abs device" role="img" aria-label="Desktop monitor and tablet displaying the credit score report dashboard"></div>

<section class="why-us">
  <h2>WHY GET YOUR SCORE <span class="accent">FROM US?</span></h2>
  <div class="abs timeline"></div>
  <div class="step" style="top:2817px">01</div>
  <div class="step-title" style="top:2833px">WE DON'T ABUSE YOUR PERSONAL INFORMATION:</div>
  <p class="step-body">Companies that give out free credit scores use your personal information to sell you financial products. That's how they can afford to give it to you for free. We believe that your personal information should be protected and not abused. That's why we ask a small fee. It enables us to protect your information and not abuse it.</p>
  <svg class="abs step-arrow" viewBox="0 0 22 22"><circle cx="11" cy="11" r="11" fill="#111"/><path d="M7 9l4 4 4-4" stroke="#fff" stroke-width="2" fill="none"/></svg>
  <div class="step" style="top:2956px">02</div>
  <div class="step-title" style="top:2972px">OUR REPORT IS SUPER EASY TO UNDERSTAND:</div>
  <div class="step" style="top:3038px">03</div>
  <div class="step-title" style="top:3054px">300,000 + SOUTH AFRICANS HAVE TRUSTED US:</div>
</section>

<footer class="abs footer"></footer>
<p class="abs footer-about" style="color:#fff">It is a long established fact that a reader will be distracted by the readable content of a page when looking at its layout. The point of using Lorem</p>
<div class="abs socials" aria-label="Social links"><i></i><i></i><i></i><i></i></div>
<ul class="abs links" style="left:458px;color:#fff"><li>HOME</li><li>ARTICLES</li><li>ABOUT US</li><li>CONTACT US</li><li>GENERAL TERMS OF USE</li><li>EXCLUSION OF LIABILITY</li></ul>
<ul class="abs links" style="left:658px;color:#fff"><li>DELIVERY POLICY</li><li>DATA POLICY</li><li>REFUND POLICY</li><li>CHARGES AND FEES</li><li>SECURITY POLICY</li><li>PRIVACY POLICY</li></ul>
<svg class="abs" style="left:843px;top:3314px" width="50" height="134" viewBox="0 0 50 134">
  <circle cx="25" cy="25" r="24" fill="none" stroke="#fff" stroke-width="2"/>
  <path d="M17 16c2-2 4-1 5 1l1 4-3 2c1 3 3 5 6 6l2-3 4 1c2 1 3 3 1 5-4 4-17-6-16-16z" fill="#fff"/>
  <circle cx="25" cy="108" r="24" fill="none" stroke="#fff" stroke-width="2"/>
  <rect x="14" y="100" width="22" height="16" rx="2" fill="#fff"/><path d="M14 101l11 8 11-8" stroke="#06142b" stroke-width="2" fill="none"/>
</svg>
<div class="abs contact-label" style="left:914px;top:3314px;color:#fff">Phone</div>
<div class="abs contact-value" style="left:915px;top:3348px;color:#fff">1-800-555-0199</div>
<div class="abs contact-label" style="left:914px;top:3394px;color:#fff">Email Address</div>
<div class="abs contact-value" style="left:914px;top:3427px;color:#fff">info@ledgermail.com</div>
<div class="abs copyright" style="color:#fff">Copyright © 2022 Bright Ledger View . All Right Reserved</div>
<a class="abs btn-demo"><svg width="32" height="26" viewBox="0 0 32 26"><path d="M2 3h18v11H9l-5 4v-4H2z" fill="none" stroke="#06142b" stroke-width="1.8"/><path d="M23 9h7v10h-2v4l-4-4h-9v-3" fill="none" stroke="#06142b" stroke-width="1.8"/></svg>LETS TALK DEMO</a>

</body>
</html>
```